Dental Practice Billboard Design

We are a newer dental practice in need of a simple but appealing billboard for our growing dental practice to attract new patients. The practice is owned by husband and wife dentists and is family friendly in a small town in Kentucky. We try to be very friendly and caring to our patients. Would prefer a blue background for the billboard and our tooth logo to be prominent. We are partial to the Patua One font used in the image below but please feel free to tweak it as you deem necessary. The shape of the uppercase D and lowercase g are why we like that font, so fonts with a similarly shaped “D” and “g” would work as well. Please include our phone number (555) 318-7092. Please see our website Halvorsenfamilydentistry.example for more info on the practice if needed. Thank you! Looking forward to seeing your creation.
Updates

The dimensions will be 12ft x 24ft (3.6576m x 7.3152m). Apologies for not including this in the original prompt. Thank you all for your submissions.

Industry/Entity Type

Dental

Font styles to use
Other font styles liked:
• Patua One

Colors
0054AA
0677BA
7BADD7
CADEEF
E8F1F8
0094D4
00A9DD
6FCCEA
C7EBF8
E9F6FB
00AB8E
00BBA5
67D7C9
C6EFE9
E9F9F6
59FF00
82FF00
B8FF75
E3FFCB
F4FFEA

Requirements
Must have
• Phone number, website, Logo, Practice name “Halvorsen Family Dentistry”
Should not have
• A tagline or slogan

```html
<!DOCTYPE html>
<html lang="en">
<head>
<meta charset="utf-8">
<title>Halvorsen Family Dentistry – Billboard</title>
<link rel="stylesheet" href="https://fonts.googleapis.com/css2?family=Patua+One&family=Fira+Sans:wght@600&family=Fira+Sans+Condensed:wght@600&display=swap">
<style>
  :root {
    --navy: #0c2b5c;
    --green: #16b11c;
    --white: #ffffff;
    --ink: #2f2f33;
    --page: #ffffff;
  }
  * { margin: 0; padding: 0; box-sizing: border-box; }
  html, body {
    width: 1071px;
    height: 1200px;
    overflow: hidden;
    background: var(--page);
  }
  .billboard {
    position: absolute;
    left: 30px;
    top: 348px;
    width: 1011px;
    height: 504px;
    background: var(--navy);
    overflow: hidden;
  }
  .billboard__bands {
    position: absolute;
    inset: 0;
  }
  .dentist-photo {
    position: absolute;
    left: 64px;
    top: 112px;
    width: 214px;
    height: 244px;
    border-radius: 38px 38px 100px 100px;
    background: linear-gradient(160deg, #c9b8a4 0%, #e9e4de 45%, #f4f4f2 70%, #2b2b2e 100%);
    border: 7px solid var(--white);
    box-shadow: 6px 4px 0 var(--green);
  }
  .practice-name {
    position: absolute;
    left: 290px;
    top: 158px;
    width: 450px;
    text-align: center;
    color: var(--white);
    font-family: "Patua One", serif;
  }
  .practice-name__main {
    display: block;
    font-size: 84px;
    line-height: 1;
    letter-spacing: 0.5px;
  }
  .practice-name__sub {
    display: block;
    margin-top: 14px;
    font-size: 44px;
    line-height: 1;
  }
  .services__title {
    position: absolute;
    right: 20px;
    top: 13px;
    color: var(--white);
    font-family: "Fira Sans Condensed", sans-serif;
    font-weight: 600;
    font-size: 30px;
    line-height: 1;
    letter-spacing: 0.3px;
  }
  .services__list {
    position: absolute;
    left: 780px;
    top: 70px;
    list-style: none;
    color: var(--white);
    font-family: "Fira Sans", sans-serif;
    font-weight: 600;
    font-size: 21px;
    line-height: 29.6px;
  }
  .services__item {
    position: relative;
    padding-left: 22px;
  }
  .services__item::before {
    content: "";
    position: absolute;
    left: 4px;
    top: 7px;
    width: 6px;
    height: 12px;
    border-right: 2px solid var(--green);
    border-bottom: 2px solid var(--green);
    transform: rotate(40deg);
  }
  .contact-web {
    position: absolute;
    left: 34px;
    top: 447px;
    display: flex;
    align-items: center;
    gap: 14px;
    color: var(--white);
    font-family: "Fira Sans", sans-serif;
    font-weight: 600;
    font-size: 27px;
    line-height: 1;
  }
  .contact-phone {
    position: absolute;
    left: 640px;
    top: 452px;
    display: flex;
    align-items: center;
    gap: 22px;
    color: var(--ink);
    font-family: "Fira Sans Condensed", sans-serif;
    font-weight: 600;
    font-size: 36px;
    line-height: 1;
  }
  .icon { display: block; flex: none; }
</style>
</head>
<body>
  <main class="billboard">
    <svg class="billboard__bands" viewBox="0 0 1011 504" width="1011" height="504" aria-hidden="true">
      <polygon points="778,0 1011,0 1011,58 737,58" fill="var(--green)"/>
      <polygon points="0,428 574,428 594,504 0,504" fill="var(--green)"/>
      <polygon points="591,442 1011,442 1011,504 610,504" fill="var(--white)"/>
    </svg>

    <div class="dentist-photo" role="img" aria-label="Photo of the two practice dentists in white coats"></div>

    <h1 class="practice-name">
      <span class="practice-name__main">Halvorsen</span>
      <span class="practice-name__sub">Family Dentistry</span>
    </h1>

    <section class="services">
      <h2 class="services__title">OUR SERVICES</h2>
      <ul class="services__list">
        <li class="services__item">Crowns</li>
        <li class="services__item">Root Canals</li>
        <li class="services__item">Extractions</li>
        <li class="services__item">Implants</li>
        <li class="services__item">Bridges</li>
        <li class="services__item">Clear Aligners</li>
        <li class="services__item">Veneers</li>
        <li class="services__item">Whitening</li>
        <li class="services__item">Fillings</li>
        <li class="services__item">Cleanings</li>
        <li class="services__item">Dentures</li>
        <li class="services__item">OverDentures</li>
      </ul>
    </section>

    <div class="contact-web">
      <svg class="icon" width="44" height="44" viewBox="0 0 44 44" aria-hidden="true">
        <circle cx="22" cy="22" r="19" fill="none" stroke="var(--white)" stroke-width="4"/>
        <ellipse cx="22" cy="22" rx="8" ry="19" fill="none" stroke="var(--white)" stroke-width="3"/>
        <line x1="3" y1="22" x2="41" y2="22" stroke="var(--white)" stroke-width="3"/>
      </svg>
      <span>Halvorsenfamilydentistry.example</span>
    </div>

    <div class="contact-phone">
      <svg class="icon" width="44" height="44" viewBox="0 0 44 44" aria-hidden="true">
        <path d="M9 5 L16 5 L19 14 L14 18 C17 25 20 28 26 31 L30 26 L39 29 L39 36 C39 39 36 41 33 40 C19 37 8 26 5 12 C4 8 6 5 9 5 Z" fill="var(--green)"/>
        <path d="M25 6 A13 13 0 0 1 38 19" fill="none" stroke="var(--green)" stroke-width="3" stroke-linecap="round"/>
        <path d="M24 12 A7 7 0 0 1 32 20" fill="none" stroke="var(--green)" stroke-width="3" stroke-linecap="round"/>
      </svg>
      <span>(555) 318-7092</span>
    </div>
  </main>
</body>
</html>
```